Re-Design Of High Traffic Content Hub

“Tarmac Compass, is a comprehensive online hub dedicated to helping over 150,000 visitors a month have a smooth towing trip. Tarmac Compass is the place where you’ll find up-to-date information, practical advice, ‘how to’ guides and handy tips for your caravan, trailer and anything else you need to tow."

Content on the site is split in to 4 main pillars:
“Caravan” “Trailer” “Boating” "Travel"

Each pillar is split further in to 3 categories:
How To • Products • Reviews

We are crowd-sourcing the redesign of the following pages:

- Home Page
- Category Page
- Single Post
- Search Results
- Static Content Page (Terms & Conditions/ About / Privacy Policy)

Look and feel to be implemented inline with UX best practice.
A strong conversion focus is desirable site wide (e-book downloads & newsletter subscriptions are offered).

Our preference is for the home page to provide the visitor with a visual snapshot of fresh site content and encourage the user to explore the site further using navigation or search.

Design elements to be featured on the home page:
Main Navigation
Site Search
Newsletter Subscription Box
eBook Download CTA
Mission Statement
2 x Recent articles from each top level content pillar including featured image and title.
An area to feature 3 of the site's best performing articles including featured image, title and excerpt.

Mission Statement: "Tarmac Compass is the place you can turn to for up-to-date information, practical advice, ‘how to’ guides and handy tips for your caravan, trailer and anything else worth towing. "

Selected designs will be coded in responsive bootstrap so preference will be given to designs presented with this in mind.

Logo's attached in transparent white and transparent dark.

Live site located at www.tarmaccompass-demo.com.au

ec1f27
f5f5f5
b2b2b2
ffffff

• Strong conversion focus (eBook downloads and newsletter subscriptions)

```html
<!DOCTYPE html>
<html lang="en">
<head>
<meta charset="utf-8">
<title>Tarmac Compass – Home</title>
<link href="https://fonts.googleapis.com/css2?family=Oswald:wght@300;400;500&display=swap" rel="stylesheet">
<style>
:root{
  --red:#ec1f27;
  --light:#f5f5f5;
  --topbar:#e6e6e6;
  --mid:#b2b2b2;
  --grey:#6d6d6d;
  --ink:#2a2a2a;
  --dark:#1c1c1c;
  --field:#2c2c2c;
  --white:#ffffff;
}
*{margin:0;padding:0;box-sizing:border-box}
html,body{width:1200px;height:2639px;overflow:hidden;background:var(--white)}
body{font-family:"Oswald",sans-serif;color:var(--ink);position:relative}
.abs{position:absolute}
.upper{text-transform:uppercase}

/* top bar */
.top-bar{left:0;top:0;width:1200px;height:48px;background:var(--topbar)}
.connect{left:171px;top:15px;font-size:11px;font-weight:300;display:flex;align-items:center;gap:6px;color:#444}
.social{display:flex;gap:5px}
.social span{width:8px;height:8px;background:var(--red);border-radius:50%;display:block}
.search{left:854px;top:12px;width:166px;height:22px;border-bottom:1px solid var(--mid);font-size:11px;font-weight:300;color:#444;display:flex;align-items:center;gap:5px}

/* logo */
.brand{display:flex;align-items:center;gap:12px}
.brand-name{font-size:30px;line-height:30px;font-weight:500;color:var(--grey);text-align:right;text-transform:uppercase}
.brand-mark{width:68px;height:96px;background:var(--red)}
.header-brand{left:162px;top:70px}

/* nav */
.main-nav{left:706px;top:70px;height:97px;display:flex;align-items:stretch}
.main-nav a{font-size:19px;color:var(--ink);text-decoration:none;text-transform:uppercase;padding:0 12px;display:flex;align-items:flex-end;padding-bottom:22px}
.main-nav a.active{background:var(--red);color:var(--white);width:84px;justify-content:center}

/* hero */
.hero-photo{left:162px;top:188px;width:586px;height:451px;background:linear-gradient(160deg,#6f6a48 0%,#c78a44 35%,#7a5a3c 60%,#5b4130 100%)}
.hero-panel{left:748px;top:188px;width:290px;height:451px;background:var(--red)}
.hero-title{left:780px;top:340px;font-size:60px;line-height:64px;color:var(--white);text-transform:uppercase;font-weight:400}
.btn-dark{background:#3a3a3a;color:var(--white);font-size:17px;text-transform:uppercase;display:flex;align-items:center;justify-content:center}
.hero-btn{left:780px;top:507px;width:104px;height:39px}
.dots{left:1011px;top:549px;display:flex;flex-direction:column;gap:9px}
.dots span{width:8px;height:9px;background:rgba(255,255,255,.45)}
.dots span:first-child{background:var(--white)}

/* pillars */
.pillar{top:639px;width:219px;height:153px;color:var(--white);font-size:14px;text-transform:uppercase}
.pillar b{font-weight:400;position:absolute;left:20px;bottom:12px}

/* section titles */
.section-title{left:0;width:1200px;text-align:center;color:var(--red);font-size:40px;text-transform:uppercase;font-weight:400}
.rule{left:162px;top:904px;width:876px;height:1px;background:#e3e3e3}

/* article cards */
.card-img{top:940px;width:270px;height:183px}
.card-title{top:1145px;font-size:15px;color:var(--red);display:flex;align-items:center;gap:10px}
.card-title i{width:20px;height:20px;background:#3a3a3a;display:flex;align-items:center;justify-content:center}
.card-text{top:1178px;width:270px;font-size:13px;line-height:23px;font-weight:300;color:var(--mid)}

/* mission */
.mission-photo{left:162px;top:1278px;width:876px;height:308px;background:linear-gradient(100deg,#8a1b17 0%,#6b2a24 28%,#6f8a47 45%,#5d8d3b 70%,#9db0a8 100%)}
.mission-panel{left:162px;top:1278px;width:268px;height:308px;background:rgba(30,10,10,.55)}
.mission-title{left:182px;top:1352px;font-size:40px;color:var(--red);text-transform:uppercase;font-weight:400}
.mission-text{left:182px;top:1412px;width:232px;font-size:10.5px;line-height:18px;color:var(--white);font-weight:300}
.mission-btn{left:182px;top:1498px;width:82px;height:22px;background:var(--white);color:var(--ink);font-size:10px;display:flex;align-items:center;justify-content:center;text-transform:uppercase}

/* recent */
.recent{top:1716px;width:426px;height:280px}
.recent-caption{left:0;bottom:0;width:100%;height:86px;background:rgba(20,20,20,.6);padding:22px 18px;color:var(--white)}
.recent-caption h3{font-size:15px;font-weight:400;text-transform:uppercase}
.recent-caption p{font-size:13px;font-weight:300;margin-top:4px}

/* conversion band */
.cta-band{left:0;top:2033px;width:1200px;height:318px;background:var(--dark)}
.news-title{left:171px;top:2070px;font-size:38px;color:var(--white);text-transform:uppercase;font-weight:400}
.news-text{left:171px;top:2128px;width:400px;font-size:10.5px;line-height:18px;color:var(--white);font-weight:300}
.news-input{left:172px;top:2205px;width:397px;height:46px;background:var(--field);color:#8a8a8a;font-size:12px;display:flex;align-items:center;padding-left:16px;text-transform:uppercase;font-weight:300}
.news-btn{left:172px;top:2267px;width:178px;height:46px;background:#000;color:var(--white);font-size:19px;display:flex;align-items:center;justify-content:center;text-transform:uppercase}
.ebook-cover{left:621px;top:2027px;width:169px;height:286px}
.ebook-title{left:804px;top:2066px;font-size:40px;line-height:46px;text-transform:uppercase;font-weight:400;color:var(--white)}
.ebook-title em{font-style:normal;color:var(--red);display:block}
.ebook-text{left:804px;top:2174px;width:190px;font-size:10px;line-height:17px;color:var(--white);font-weight:300}
.ebook-btn{left:804px;top:2268px;width:176px;height:45px;background:var(--red);color:var(--white);font-size:17px;display:flex;align-items:center;justify-content:center;text-transform:uppercase}

/* footer */
.footer-brand{left:162px;top:2394px}
.footer-col{top:2394px;font-size:11px;font-weight:300;color:#444}
.footer-col h4{font-size:11px;color:var(--red);text-transform:uppercase;font-weight:400;margin-bottom:12px}
.footer-col li{list-style:none;line-height:26.5px}
.footer-rule{left:0;top:2578px;width:1200px;height:1px;background:#e3e3e3}
.copyright{left:162px;top:2598px;font-size:10.5px;font-weight:300;color:#444}
.footer-connect{left:896px;top:2598px;font-size:10.5px;font-weight:300;color:#444;display:flex;gap:6px;align-items:center}
.to-top{left:1166px;top:2598px;font-size:10px;color:#777}
</style>
</head>
<body>

<div class="abs top-bar"></div>
<div class="abs connect upper">Connect with us
  <div class="social"><span></span><span></span><span></span><span></span><span></span></div>
</div>
<div class="abs search upper">
  <svg width="10" height="10" viewBox="0 0 10 10"><circle cx="4" cy="4" r="3" fill="none" stroke="#ec1f27" stroke-width="1.5"/><line x1="6.2" y1="6.2" x2="9" y2="9" stroke="#ec1f27" stroke-width="1.5"/></svg>
  Search
</div>

<div class="abs brand header-brand">
  <div class="brand-name">Tarmac<br>Compass</div>
  <div class="brand-mark"></div>
</div>

<nav class="abs main-nav">
  <a class="active" href="#">Caravan</a>
  <a href="#">Trailer</a>
  <a href="#">Boating</a>
  <a href="#">Travel</a>
</nav>

<div class="abs hero-photo" role="img" aria-label="Portable red generator on a dusty campsite at sunset beside a parked vehicle"></div>
<div class="abs hero-panel"></div>
<h1 class="abs hero-title">Tarmac<br>Compass</h1>
<div class="abs btn-dark hero-btn">Learn more</div>
<div class="abs dots"><span></span><span></span><span></span><span></span></div>

<div class="abs pillar" style="left:162px;background:linear-gradient(135deg,#4f7a33,#9fb77a 60%,#d8d8d0)" role="img" aria-label="Caravan parked on grass under trees"><b>Caravan</b></div>
<div class="abs pillar" style="left:381px;background:linear-gradient(135deg,#9fa6a8,#dfe3e3 50%,#7d8689)" role="img" aria-label="Close-up of a trailer hitch"><b>Trailers</b></div>
<div class="abs pillar" style="left:600px;background:linear-gradient(180deg,#8fb2d1,#d7e1ea 55%,#7f8a8f)" role="img" aria-label="Boat on a trailer by a lake"><b>Boats</b></div>
<div class="abs pillar" style="left:819px;background:linear-gradient(160deg,#2f4a26,#5d7d3e 55%,#3b3428)" role="img" aria-label="Road through a forest with a vehicle"><b>Travel</b></div>

<h2 class="abs section-title" style="top:830px">Articles</h2>
<div class="abs rule"></div>

<div class="abs card-img" style="left:172px;background:linear-gradient(180deg,#6aa8d8,#cfe6f0 45%,#e8dcc0 70%,#b89a6c)" role="img" aria-label="Traveller standing on a beach boardwalk"></div>
<div class="abs card-img" style="left:465px;background:linear-gradient(180deg,#6e5430,#b08a5c 50%,#c9a777)" role="img" aria-label="Children inside a caravan cupboard"></div>
<div class="abs card-img" style="left:759px;background:linear-gradient(135deg,#c9c9c9,#f0f0f0 45%,#7d7d7d)" role="img" aria-label="Close-up of a caravan suspension coil spring"></div>

<div class="abs card-title" style="left:172px"><i><svg width="8" height="8" viewBox="0 0 8 8"><path d="M2 1l4 3-4 3z" fill="#fff"/></svg></i>How To Theft-Proof Your Caravan</div>
<div class="abs card-title" style="left:465px"><i><svg width="8" height="8" viewBox="0 0 8 8"><path d="M2 1l4 3-4 3z" fill="#fff"/></svg></i>How To Theft-Proof Your Caravan</div>
<div class="abs card-title" style="left:759px"><i><svg width="8" height="8" viewBox="0 0 8 8"><path d="M2 1l4 3-4 3z" fill="#fff"/></svg></i>How To Theft-Proof Your Caravan</div>
<p class="abs card-text" style="left:172px">Want to ensure your caravan is virtually theft-proof? The Rolvek TS 2.0 is the answer.</p>
<p class="abs card-text" style="left:465px">Want to ensure your caravan is virtually theft-proof? The Rolvek TS 2.0 is the answer.</p>
<p class="abs card-text" style="left:759px">Want to ensure your caravan is virtually theft-proof? The Rolvek TS 2.0 is the answer.</p>

<div class="abs mission-photo" role="img" aria-label="Vehicle tow bar and gas bottle on a trailer in a green park"></div>
<div class="abs mission-panel"></div>
<h2 class="abs mission-title">Mission</h2>
<p class="abs mission-text">Tarmac Compass is the place you can turn to for up-to-date information, practical advice, ‘how to’ guides and handy tips for your caravan, trailer and anything else worth towing.</p>
<div class="abs mission-btn">Learn more</div>

<h2 class="abs section-title" style="top:1632px">Recent Articles</h2>

<article class="abs recent" style="left:162px;background:linear-gradient(180deg,#5b9fe0,#cfe3f3 35%,#9fc46a 60%,#4f8a2b)" role="img" aria-label="White caravan on a sunny green field">
  <div class="abs recent-caption"><h3>Caravanning with kids</h3><p>How to go caravanning with kids – and have a great time!</p></div>
</article>
<article class="abs recent" style="left:612px;background:linear-gradient(150deg,#fbe7c8,#f3b46a 45%,#d88a4a 75%,#8f6e58)" role="img" aria-label="Traveller reading a map in warm sunlight">
  <div class="abs recent-caption"><h3>Splashing out: the pros of buying a prestige caravan</h3><p>How to go caravanning with kids – and have a great time!</p></div>
</article>

<section class="abs cta-band"></section>
<h2 class="abs news-title">Free Weekly Newsletters</h2>
<p class="abs news-text">Tarmac Compass is the place you can turn to for up-to-date information, practical advice, ‘how to’ guides and handy tips for your caravan, trailer and anything else worth towing. To receive regular towing hints, tips sign up to our newsletter today!</p>
<div class="abs news-input">Enter your e-mail address</div>
<div class="abs news-btn">Subscribe now !</div>

<div class="abs ebook-cover" style="background:linear-gradient(90deg,#ec1f27 0 38%,#6b7a70 38%,#a3a9a2 70%,#5d6659)" role="img" aria-label="E-book cover with towing photographs"></div>
<h2 class="abs ebook-title"><em>eBook</em>Download</h2>
<p class="abs ebook-text">Whether you’re a novice or an experienced caravan holiday-maker, our towing e-book with essential safety, preparation and towing tips will be the perfect driving companion.</p>
<div class="abs ebook-btn">E-book download</div>

<div class="abs brand footer-brand">
  <div class="brand-name">Tarmac<br>Compass</div>
  <div class="brand-mark"></div>
</div>

<div class="abs footer-col" style="left:384px"><h4>Categories</h4><ul><li>Caravan</li><li>Trailers</li><li>Boats</li><li>Travel</li></ul></div>
<div class="abs footer-col" style="left:517px"><h4>Tags</h4><ul><li>Caravan Safe</li><li>Replace Trailer Lights</li><li>Caravan Tv Antenna</li><li>Masthead Lights</li><li>Manual vs Auto</li></ul></div>
<div class="abs footer-col" style="left:663px"><h4>Popular</h4><ul><li>5 Tips For Hitching Up Your Caravan</li><li>How To Stay Snug Whilst Caravanning This Winter</li><li>How To Theft-Proof Your Caravan</li><li>Continuing to Work Whilst You’re on the Road</li><li>Where can you park your caravan?</li></ul></div>
<div class="abs footer-col" style="left:901px"><h4>Recommended</h4><ul><li>Is Your Caravan ‘Fire Ready’?</li></ul></div>

<div class="abs footer-rule"></div>
<p class="abs copyright">© 2016 Company Name | All Rights Reserved</p>
<div class="abs footer-connect">Connect With Us <div class="social"><span></span><span></span><span></span><span></span><span></span></div></div>
<div class="abs to-top">
  <svg width="12" height="10" viewBox="0 0 12 10"><path d="M1 8l5-5 5 5" fill="none" stroke="#777" stroke-width="1.5"/></svg>
</div>

</body>
</html>
```